Business card design needed

Business Card design required for new small plumbing business.
Would like a logo/text look that is simple and unique and does not have to be representative of a plumbing company (ie. having a cartoon plumber or toilet etc) as the companyname is self explanatory.
Would like the main colour to be green (lime green).

Industry/Entity Type

Plumber

Contact Information for Business Card

BRISCOMB PLUMBING
ABN 61 947 205 318 004

Harold Tenfield
Licensed Plumber 71635
Phone: 0477 261 408

27 Worrell Drive,
Kelbrook. 3962 Westvale

Email: briscombplumbing@mailora.net

Logo Text

Briscomb Plumbing

Logo styles of interest
Character Logo
Wordmark Logo
Lettermark Logo

```html
<!DOCTYPE html>
<html lang="en">
<head>
<meta charset="utf-8">
<title>Briscomb Plumbing – Business Card</title>
<link rel="stylesheet" href="https://fonts.googleapis.com/css2?family=Tinos:wght@400;700&family=Questrial&display=swap">
<style>
  :root {
    --lime: #74f800;
    --lime-panel: #8cff00;
    --navy: #14107a;
    --ink: #161a6e;
    --stripe: #1b1b1b;
  }
  html, body {
    margin: 0;
    padding: 0;
    width: 1200px;
    height: 741px;
    overflow: hidden;
    background: var(--lime);
  }
  .card {
    position: relative;
    width: 1200px;
    height: 741px;
    overflow: hidden;
    background: var(--lime);
  }
  .texture {
    position: absolute;
  }
  .texture--top-right {
    left: 740px;
    top: 0;
    width: 460px;
    height: 200px;
    background: radial-gradient(ellipse at 65% 35%, rgba(47, 90, 16, 0.45), rgba(47, 90, 16, 0) 70%);
  }
  .texture--bottom-left {
    left: 0;
    top: 350px;
    width: 340px;
    height: 391px;
    background: radial-gradient(ellipse at 30% 50%, rgba(47, 90, 16, 0.45), rgba(47, 90, 16, 0) 72%);
  }
  .stripes {
    position: absolute;
    left: 0;
    top: 0;
  }
  .panel {
    position: absolute;
    background: var(--lime-panel);
  }
  .panel--brand {
    left: 0;
    top: 63px;
    width: 474px;
    height: 295px;
    border-top-right-radius: 8px;
  }
  .panel--contact {
    left: 324px;
    top: 192px;
    width: 876px;
    height: 332px;
  }
  .brand {
    position: absolute;
    left: 72px;
    top: 146px;
    margin: 0;
    font-family: "Tinos", serif;
    font-weight: 700;
    color: var(--navy);
    line-height: 1;
    text-transform: uppercase;
  }
  .brand__name {
    display: block;
    font-size: 62px;
    letter-spacing: 2px;
  }
  .brand__trade {
    display: block;
    margin-top: 26px;
    font-size: 44px;
    letter-spacing: 1px;
  }
  .person {
    position: absolute;
    left: 614px;
    top: 252px;
    margin: 0;
    font-family: "Tinos", serif;
    font-weight: 400;
    font-size: 52px;
    color: var(--navy);
    line-height: 1;
  }
  .details {
    position: absolute;
    left: 614px;
    top: 338px;
    margin: 0;
    padding: 0;
    list-style: none;
    font-family: "Questrial", sans-serif;
    font-size: 29px;
    line-height: 41px;
    color: var(--ink);
  }
  .abn {
    position: absolute;
    right: 30px;
    top: 630px;
    margin: 0;
    font-family: "Tinos", serif;
    font-size: 29px;
    color: var(--ink);
  }
  .email {
    position: absolute;
    right: 26px;
    top: 680px;
    margin: 0;
    font-family: "Questrial", sans-serif;
    font-size: 29px;
    color: var(--ink);
  }
</style>
</head>
<body>
<main class="card">
  <div class="texture texture--top-right" role="img" aria-label="Dark green smoky abstract texture"></div>
  <div class="texture texture--bottom-left" role="img" aria-label="Dark green smoky abstract texture"></div>

  <svg class="stripes" width="180" height="60" viewBox="0 0 180 60" aria-hidden="true">
    <defs>
      <pattern id="hatch" width="12" height="12" patternUnits="userSpaceOnUse" patternTransform="rotate(45)">
        <rect width="5" height="12" fill="var(--stripe)"/>
      </pattern>
    </defs>
    <rect width="180" height="60" fill="url(#hatch)"/>
  </svg>

  <div class="panel panel--brand"></div>
  <div class="panel panel--contact"></div>

  <h1 class="brand">
    <span class="brand__name">Briscomb</span>
    <span class="brand__trade">Plumbing</span>
  </h1>

  <h2 class="person">Harold Tenfield</h2>
  <ul class="details">
    <li>Licensed Plumber 71635</li>
    <li>Phone: 0477 261 408 27</li>
    <li>Worrell Drive, Kelbrook. 3962 Westvale</li>
  </ul>

  <p class="abn">ABN 61 947 205 318 004</p>
  <p class="email">Email: briscombplumbing@mailora.net</p>
</main>
</body>
</html>
```